Entertainer/Dancer Business Cards

Devon Marsh is an up and coming entertainer from Baltimore, Maryland currently relocating to Los Angeles, California for a dance opportunity at the renowned Ruthie Calder Dance Studio.
This young man needs to promote himself and his skills in a populous and competitive city.
Hopefully, this card will set him apart from the tons of entertainers in L.A.
It will passed out to fellow entertainers, agents, and random people looking for talent.

I have uploaded an image of the dancer, it is not necessary to use this image; however it is in PSD format if one should decide to incorporate it somehow and would like to make changes.

Industry/Entity Type

Business

Contact Information for Business Card

Devon Marsh
(line 1) Dancer Choreographer Instructor Singer/Songwriter
(line 2) Ballet-Modern-Urban
devonmarsh00@fernpost.com
410-582-7146

Requirements
Nice to have

• Open to an all typography card.
Should not have
• No logo; just name: Devon Marsh
Devon is a guy (in case you were wondering :D )
Please no ballet/pointe shoes in design

```html
<!DOCTYPE html>
<html lang="en">
<head>
<meta charset="utf-8">
<title>Devon Marsh — Business Card</title>
<link rel="stylesheet" href="https://fonts.googleapis.com/css2?family=Josefin+Sans:wght@400;500&display=swap">
<style>
  :root {
    --paper: #ffffff;
    --ink: #000000;
    --ribbon-light: #f1f1f1;
    --ribbon-mid: #cfcfcf;
  }
  html, body {
    margin: 0;
    padding: 0;
    width: 1200px;
    height: 702px;
    overflow: hidden;
    background: var(--paper);
  }
  .card {
    position: relative;
    width: 1200px;
    height: 702px;
    background: var(--paper);
    color: var(--ink);
    font-family: "Josefin Sans", "Futura", sans-serif;
    font-variant: small-caps;
    overflow: hidden;
  }
  .contact {
    position: absolute;
    left: 40px;
    top: 36px;
  }
  .contact__name {
    margin: 0;
    font-size: 66px;
    font-weight: 400;
    line-height: 1;
    letter-spacing: 1px;
  }
  .contact__email,
  .contact__phone {
    margin: 0;
    font-size: 36px;
    font-weight: 400;
    line-height: 1;
    letter-spacing: 1px;
  }
  .contact__email { margin-top: 22px; }
  .contact__phone { margin-top: 20px; }

  .ribbon-art {
    position: absolute;
    left: 756px;
    top: 39px;
    width: 422px;
    height: 512px;
    border-radius: 46% 40% 48% 42%;
    background: radial-gradient(ellipse at 55% 45%, var(--ribbon-mid) 0%, var(--ribbon-light) 60%, var(--paper) 100%);
  }

  .skills {
    position: absolute;
    left: 0;
    right: 0;
    top: 576px;
    text-align: center;
  }
  .skills__roles,
  .skills__styles {
    margin: 0;
    font-size: 44px;
    font-weight: 400;
    line-height: 1;
    letter-spacing: 0.5px;
  }
  .skills__styles { margin-top: 14px; }
</style>
</head>
<body>
  <main class="card">
    <section class="contact">
      <h1 class="contact__name">Devon Marsh</h1>
      <p class="contact__email">devonmarsh00@fernpost.com</p>
      <p class="contact__phone">410-582-7146</p>
    </section>

    <div class="ribbon-art" role="img" aria-label="Flowing black calligraphic ribbon illustration suggesting a dancer in motion"></div>

    <section class="skills">
      <p class="skills__roles">Dancer Choreographer Instructor Singer/Songwriter</p>
      <p class="skills__styles">Ballet-Modern-Urban</p>
    </section>
  </main>
</body>
</html>
```